Webdesign für Immobilienmanagement
Zielgruppe
Immobilienmanagement Unternehmen / allg. Hausverwaltung , Hausmeisterservice, Grünanlagenpflege, Unterhaltsreinigung, Winterdienst
Zielgruppe: Mieter und Wohnungseigentümer
Aufgabenstellung
Farben: weiß/grün
keine Kopie der alten Seite
nutzerfreundliche Unternehmenswebseite
Logo vorhanden auf alter Webseite

```html
<!DOCTYPE html>
<html lang="de">
<head>
<meta charset="utf-8">
<title>Grünhof Immobilien-Management</title>
<link href="https://fonts.googleapis.com/css2?family=Lato:wght@300;400;700;900&display=swap" rel="stylesheet">
<style>
:root{
  --green:#4fa62f;
  --green-dark:#3b8a22;
  --forest:#17280c;
  --footer-top:#1e3d0f;
  --footer-bottom:#2f6a1a;
  --yellow:#f7c11c;
  --text:#333;
  --muted:#555;
  --light:#f4f5f3;
  --line:#e2e2e2;
}
*{box-sizing:border-box;margin:0;padding:0}
html,body{width:1200px;height:3316px;overflow:hidden}
body{font-family:'Lato',sans-serif;color:var(--text);background:#fff;position:relative}
.abs{position:absolute}

/* top bar */
.topbar{left:0;top:0;width:1200px;height:49px;background:var(--forest)}
.emergency{left:762px;top:0;width:287px;height:49px;background:var(--yellow);display:flex;align-items:center;padding:0 12px;gap:14px;color:#1a1a1a}
.emergency .info{font-size:10px;line-height:12px;width:140px}
.emergency .info b{display:block;font-weight:900}
.emergency .sep{width:1px;height:30px;background:#8a6b00}
.emergency .hours{display:flex;align-items:center;gap:8px;font-size:10px;line-height:12px;font-weight:700}

/* header */
.brand{left:149px;top:66px;display:flex;flex-direction:column}
.brand .name{display:flex;align-items:center;gap:8px;font-size:26px;font-weight:700;color:var(--green);letter-spacing:1px}
.brand .name span.mark{width:22px;height:22px;background:var(--green)}
.brand .sub{font-size:8px;color:#333;letter-spacing:.3px;margin-top:2px}
.nav{left:438px;top:49px;height:66px;display:flex;gap:0}
.nav a{display:block;padding:0 13px;line-height:70px;font-size:13px;color:#222;text-decoration:none;position:relative}
.nav a.active{color:var(--green);font-weight:700}
.nav a.active::after{content:"";position:absolute;left:0;right:0;bottom:-3px;height:3px;background:var(--green)}

/* hero */
.hero{left:0;top:129px;width:1200px;height:418px;background:linear-gradient(90deg,#f1f1f1,#fafafa 60%,#eef0ef)}
.hero-title{left:150px;top:218px;font-size:46px;line-height:54px;font-weight:300;color:#555}
.hero-title strong{display:block;font-weight:900;color:var(--green)}
.hero-visual{left:445px;top:142px;width:720px;height:386px;background:linear-gradient(160deg,#e7e4df 0%,#8f6a4c 45%,#4e4a45 70%,#7aa35a 100%);clip-path:polygon(15% 20%,55% 0,80% 8%,100% 35%,100% 70%,60% 100%,5% 80%)}
.dots{left:567px;top:523px;display:flex;gap:7px}
.dots i{width:7px;height:7px;border-radius:50%;background:var(--yellow)}
.dots i:first-child{background:var(--green)}

/* about */
.about-visual{left:151px;top:520px;width:353px;height:334px;background:linear-gradient(180deg,#8cc3e8 0%,#cfe3ef 35%,#8aa0a8 55%,#5fa134 70%,#8ccb3e 100%);clip-path:polygon(0 0,100% 0,100% 92%,0 100%)}
.about{left:564px;top:614px;width:470px}
.section-title{font-size:26px;font-weight:400;color:var(--green)}
.about p{font-size:12px;line-height:18px;color:#333;margin-top:16px}
.about p + p{margin-top:18px}

.center-title{left:0;width:1200px;text-align:center}

/* services */
.card{width:401px}
.card .photo{width:401px;height:238px}
.card h3{font-size:16px;font-weight:400;color:var(--green);margin-top:18px;letter-spacing:.3px}
.card ul{list-style:none;display:grid;grid-template-columns:197px 197px;margin-top:9px;row-gap:4px;font-size:11px;color:#333;grid-auto-flow:column;grid-template-rows:14px 14px}
.card ul.wide{grid-template-columns:173px 200px}
.card li::before{content:"»";color:#777;margin:0 7px 0 2px}
.btn-more{display:inline-block;margin:16px 0 0 4px;width:73px;height:22px;background:var(--green);color:#fff;font-size:11px;font-weight:700;line-height:22px;padding-left:16px}

/* why */
.why-band{left:0;top:2286px;width:1200px;height:225px;background:#f7f7f6;border-top:1px solid var(--line)}
.why-box{left:151px;top:2370px;width:898px;height:110px;background:#fff;border:1px solid var(--line);display:flex;align-items:center}
.why-item{flex:auto;text-align:center;border-right:1px solid var(--line);height:84px;display:flex;flex-direction:column;align-items:center;justify-content:flex-start;padding-top:4px;font-size:12px;line-height:14px;color:#333}
.why-item:last-child{border-right:0}
.why-item .icon{width:38px;height:38px;margin-bottom:9px}

/* testimonials */
.reviews{left:0;top:2511px;width:1200px;height:474px;background:linear-gradient(180deg,#eef2ec 0%,#f6f8f5 40%,#e4e9e2 75%,#c9d6c2 100%)}
.skyline{left:0;top:2790px;width:1200px;height:195px;background:linear-gradient(180deg,rgba(200,208,205,0) 0%,rgba(190,198,196,.55) 55%,rgba(130,170,110,.6) 100%)}
.reviews-title{font-size:26px;font-weight:700;color:#222}
.arrow{width:30px;height:30px;border-radius:50%;background:var(--yellow);display:flex;align-items:center;justify-content:center}
.review{width:420px;display:flex;gap:18px}
.avatar-wrap{position:relative;width:68px;flex:none}
.avatar{width:68px;height:68px;border-radius:50%;background:linear-gradient(135deg,#c9a088,#8b6a58)}
.quote-badge{position:absolute;left:-4px;top:-8px;width:24px;height:24px;border-radius:50%;background:var(--green);color:#fff;font-size:18px;font-weight:900;line-height:30px;text-align:center}
.review p{font-size:12px;line-height:18px;color:#444}
.stars{color:var(--yellow);font-size:14px;letter-spacing:5px;margin-top:14px}
.review .who{font-size:13px;font-weight:700;color:#222;margin-top:4px;margin-left:4px}

/* footer */
.footer{left:0;top:2985px;width:1200px;height:331px;background:linear-gradient(180deg,var(--footer-top),var(--footer-bottom))}
.f-head{font-size:12px;font-weight:700;color:var(--yellow);letter-spacing:.3px}
.f-contact{left:151px;top:3012px;color:#fff;font-size:11px;line-height:18px}
.f-row{display:flex;gap:12px;align-items:flex-start;margin-top:12px}
.f-row svg{flex:none;margin-top:2px}
.f-links{left:443px;top:3012px}
.f-links ul{list-style:none;margin-top:20px;font-size:11px;line-height:18px;color:#fff}
.f-member{left:606px;top:3012px;width:160px}
.member-mark{width:52px;height:52px;border-radius:50%;border:3px solid #fff;margin-top:16px}
.f-member .t{font-size:10px;color:#fff;margin-top:16px}
.f-member .s{font-size:9px;line-height:11px;color:var(--green);margin-top:6px}
.callback{left:814px;top:3034px;width:230px}
.callback h4{font-size:17px;font-weight:700;color:var(--yellow)}
.callback p{font-size:10px;line-height:12px;color:#fff;margin:6px 0 18px 4px}
.field{height:26px;border-radius:13px;background:#fff;font-size:11px;color:#333;line-height:26px;padding-left:18px;margin-bottom:12px}
.send{height:26px;border-radius:13px;background:var(--yellow);font-size:12px;font-weight:700;line-height:26px;text-align:center;color:#222}
</style>
</head>
<body>

<div class="abs topbar"></div>
<div class="abs emergency">
  <div class="info"><b>NOTDIENST</b>24 Std. am Tag und auch an den Wochenenden!</div>
  <div class="sep"></div>
  <div class="hours">
    <svg width="18" height="18" viewBox="0 0 24 24" fill="none" stroke="#1a1a1a" stroke-width="2"><circle cx="12" cy="12" r="9"/><path d="M12 7v5l3 2"/></svg>
    <span>24 STD<br>NOTDIENST</span>
  </div>
</div>

<div class="abs brand">
  <div class="name"><span>GRÜNHOF</span><span class="mark"></span></div>
  <div class="sub">IMMOBILIEN - MANAGEMENT GMBH</div>
</div>
<nav class="abs nav">
  <a class="active">Home</a><a>Uber uns</a><a>Hausverwaltung</a><a>Hausmeister</a><a>Downloads</a><a>Partnerlinks</a><a>Kontakt</a>
</nav>

<div class="abs hero"></div>
<div class="abs hero-visual" role="img" aria-label="Moderne Architekturvilla mit Holzfassade, Glasflächen und Grünpflanzen"></div>
<h1 class="abs hero-title">Ihr zuverlässiger<strong>Dienstleister rund</strong>um die Immobilie</h1>
<div class="abs dots"><i></i><i></i><i></i><i></i><i></i></div>

<div class="abs about-visual" role="img" aria-label="Hochhäuser hinter einer grünen Wiese unter blauem Himmel"></div>
<section class="abs about">
  <h2 class="section-title">Wer wir sind</h2>
  <p>Wir sind ein junges, freundliches, gut ausgebildetes Team, das sich mit all seiner Aufmerksamkeit und Kompetenz um Ihre Wünsche in Sachen Immobilien kümmert. Möchten Sie eine Wohnung mieten, suchen Sie einen Hausmeister ... oder einen Verwalter für Ihre Immobilie?</p>
  <p>Schauen Sie sich unser Leistungsangebot an und überzeugen Sie sich selbst von den Vorteilen, die wir Ihnen bieten können.</p>
</section>

<h2 class="abs center-title section-title" style="top:945px">Was wir tun</h2>

<article class="abs card" style="left:151px;top:1025px">
  <div class="photo" role="img" aria-label="Gelbes Holzhaus mit Garten und Baum" style="background:linear-gradient(180deg,#d9dfd6,#d8b46a 45%,#6f8d45 100%)"></div>
  <h3>HAUSVERWALTUNG</h3>
  <ul><li>Allgemeine Verwaltung</li><li>Kaufmännische Betreuung</li><li>Technische Betreuung</li></ul>
  <a class="btn-more">Mehr ...</a>
</article>
<article class="abs card" style="left:645px;top:1025px">
  <div class="photo" role="img" aria-label="Zwei Bauarbeiter mit Helm und Warnweste prüfen Pläne" style="background:linear-gradient(135deg,#8c9396,#d98a2a 50%,#c9ccce 100%)"></div>
  <h3>HAUSMEISTER</h3>
  <ul class="wide"><li>Hausmeisterservice</li><li>Grünanlagenpflege</li><li>Winterdienst</li><li>Unterhaltsreinigung</li></ul>
  <a class="btn-more">Mehr ...</a>
</article>

<article class="abs card" style="left:151px;top:1437px">
  <div class="photo" role="img" aria-label="Handwerker repariert Abfluss unter einer Spüle" style="background:linear-gradient(135deg,#cfc9c0,#7a6b5a 40%,#2b4aa8 70%,#e4e0d8 100%)"></div>
  <h3>NOTDIENST</h3>
  <ul><li>Schnell &amp; kompetent</li><li>24 Stunden am Tag, 7 Tage die Woche</li></ul>
  <a class="btn-more">Mehr ...</a>
</article>
<article class="abs card" style="left:645px;top:1437px">
  <div class="photo" role="img" aria-label="Sonnige Parkwiese mit Bäumen vor Stadtsilhouette" style="background:linear-gradient(180deg,#f2e6b8,#e8c86a 40%,#86a13a 62%,#5f8e2a 100%)"></div>
  <h3>GRÜNANLAGENPFLEGE</h3>
  <ul class="wide"><li>Hausmeisterservice</li><li>Grünanlagenpflege</li><li>Winterdienst</li><li>Unterhaltsreinigung</li></ul>
  <a class="btn-more">Mehr ...</a>
</article>

<article class="abs card" style="left:151px;top:1857px">
  <div class="photo" role="img" aria-label="Reinigungskraft mit Reinigungswagen im Büro" style="background:linear-gradient(90deg,#e6e6e4,#9a9a98 45%,#4a4a48 60%,#d6c5b2 100%)"></div>
  <h3>UNTERHALTSREINIGUNG</h3>
  <ul><li>Schnell &amp; kompetent</li><li>24 Stunden am Tag, 7 Tage die Woche</li></ul>
  <a class="btn-more">Mehr ...</a>
</article>
<article class="abs card" style="left:645px;top:1857px">
  <div class="photo" role="img" aria-label="Modernes Haus in verschneiter Winterlandschaft" style="background:linear-gradient(180deg,#c9d6dc,#8e9a96 45%,#e9eef0 80%,#ffffff 100%)"></div>
  <h3>WINTERDIENST</h3>
  <ul class="wide" style="grid-template-columns:188px 200px"><li>Hausmeisterservice</li><li>Grünanlagenpflege</li><li>Winterdienst</li><li>Unterhaltsreinigung</li></ul>
  <a class="btn-more">Mehr ...</a>
</article>

<div class="abs why-band"></div>
<h2 class="abs center-title section-title" style="top:2314px">Warum uns wählen</h2>
<div class="abs why-box">
  <div class="why-item"><div class="icon" role="img" aria-label="Symbol Verwaltung" style="border:2px solid var(--green);border-radius:6px"></div>Allgemeine<br>Hausverwaltung</div>
  <div class="why-item"><div class="icon" role="img" aria-label="Symbol Beratung" style="border:2px solid var(--green);border-radius:50%"></div>Kaufmännische<br>Betreuung</div>
  <div class="why-item"><div class="icon" role="img" aria-label="Symbol Technik" style="border:2px solid var(--green);border-radius:6px"></div>Technische<br>Betreuung</div>
  <div class="why-item"><div class="icon" role="img" aria-label="Symbol Werkzeug" style="border:2px solid var(--green);border-radius:6px"></div>Hausmeisterservice</div>
  <div class="why-item"><div class="icon" role="img" aria-label="Symbol Gartenpflege" style="border:2px solid var(--green);border-radius:6px"></div>Grünanlagenpflege</div>
  <div class="why-item"><div class="icon" role="img" aria-label="Symbol Reinigung" style="border:2px solid var(--green);border-radius:6px"></div>Unterhaltsreinigung</div>
  <div class="why-item"><div class="icon" role="img" aria-label="Symbol Schneeflocke" style="border:2px solid var(--green);border-radius:50%"></div>Winterdienst</div>
</div>

<div class="abs reviews"></div>
<div class="abs skyline" role="img" aria-label="Blasse Stadtsilhouette mit Hochhäusern"></div>
<h2 class="abs center-title reviews-title" style="top:2558px">Was unser Kunde sagt</h2>
<div class="abs arrow" style="left:93px;top:2662px"><svg width="12" height="12" viewBox="0 0 12 12" fill="none" stroke="#fff" stroke-width="2"><path d="M8 2 4 6l4 4"/></svg></div>
<div class="abs arrow" style="left:1077px;top:2662px"><svg width="12" height="12" viewBox="0 0 12 12" fill="none" stroke="#fff" stroke-width="2"><path d="M4 2l4 4-4 4"/></svg></div>

<div class="abs review" style="left:157px;top:2644px">
  <div class="avatar-wrap"><div class="avatar" role="img" aria-label="Porträt einer Kundin"></div><div class="quote-badge">“</div></div>
  <div>
    <p>Lorem ipsum dolor sit amet, consectetur adipiscing elit, sed do eiusmod tempor incididunt ut labore et dolore magna aliqua. Quis ipsum suspendisse ultrices gravida. Risus commodo viverra maecenas accumsan lacus vel facilisis.</p>
    <div class="stars">★★★★★</div>
    <div class="who">- Jonas Weber</div>
  </div>
</div>
<div class="abs review" style="left:607px;top:2644px;width:430px">
  <div class="avatar-wrap"><div class="avatar" role="img" aria-label="Porträt eines Kunden" style="background:linear-gradient(135deg,#d0b8a6,#5d5a58)"></div><div class="quote-badge">“</div></div>
  <div>
    <p>Lorem ipsum dolor sit amet, consectetur adipiscing elit, sed do eiusmod tempor incididunt ut labore et dolore magna aliqua. Quis ipsum suspendisse ultrices gravida. Risus commodo viverra maecenas accumsan lacus vel facilisis.</p>
    <div class="stars">★★★★★</div>
    <div class="who">- Jonas Weber</div>
  </div>
</div>

<footer class="abs footer"></footer>
<div class="abs f-contact">
  <div class="f-head">KONTAKT</div>
  <div class="f-row" style="margin-top:20px">
    <svg width="14" height="18" viewBox="0 0 14 18"><path d="M7 0a7 7 0 0 1 7 7c0 5-7 11-7 11S0 12 0 7a7 7 0 0 1 7-7z" fill="var(--yellow)"/><circle cx="7" cy="7" r="2.5" fill="#1e3d0f"/></svg>
    <div>Grünhof Immobilien-Management GmbH<br>Lindenweg 8 b<br>04600 Musterstadt</div>
  </div>
  <div class="f-row" style="margin-top:10px"><svg width="14" height="14" viewBox="0 0 24 24" fill="none" stroke="var(--yellow)" stroke-width="2"><path d="M5 3h4l2 5-3 2a11 11 0 0 0 6 6l2-3 5 2v4a2 2 0 0 1-2 2A18 18 0 0 1 3 5a2 2 0 0 1 2-2z"/></svg><div>03400/123-0</div></div>
  <div class="f-row" style="margin-top:4px"><svg width="14" height="14" viewBox="0 0 24 24" fill="none" stroke="var(--yellow)" stroke-width="2"><path d="M6 9V3h12v6M6 18H3v-8h18v8h-3M6 14h12v7H6z"/></svg><div>03400/123-45</div></div>
  <div class="f-row" style="margin-top:4px"><svg width="14" height="14" viewBox="0 0 24 24" fill="none" stroke="var(--yellow)" stroke-width="2"><rect x="2" y="5" width="20" height="14"/><path d="m2 5 10 8 10-8"/></svg><div>info@gruenhof-immobilien.de</div></div>
</div>
<div class="abs f-links">
  <div class="f-head">QUICKLINKS</div>
  <ul><li>Home</li><li>Uber uns</li><li>Hausverwaltung</li><li>Hausmeister</li><li>Downloads</li><li>Partnerlinks</li><li>Kontakt</li><li>Impressum</li><li>Datenschutz</li></ul>
</div>
<div class="abs f-member">
  <div class="f-head">MITGLIEDSCHAFT</div>
  <div class="member-mark"></div>
  <div class="t">Wir sind Mitglied ...</div>
  <div class="s">Verband der Hausverwalter Mittelland e.V.</div>
</div>
<div class="abs callback">
  <h4>Fordern Sie einen Rückruf an</h4>
  <p>Sie haben eine Frage zu unserem Serviceangebot? Dann füllen Sie einfach folgendes Formular aus und wir melden uns schnellst-möglich bei Ihnen.</p>
  <div class="field">Name:</div>
  <div class="field">E-Mail:</div>
  <div class="field">Telefon:</div>
  <div class="send">SENDEN</div>
</div>

</body>
</html>
```